Copper Lantern Stationery Design COMMITTED PAY

We need you to design stationary for a new Business called Copper Lantern. We have already got the logo designed and it is attached. Obviously we're looking for a stationery set designed around the colours and style to match the logo.

Use generic name, address, phone, fax, email etc ... I will edit text to required details.

What we need:
- Business Card Design Double Sided (90 x 55m + Bleed 3mm+)
- A4 Letter head Design
- A4 Presentation Folder Design
- Invoice Header Approx 210 x 55mm (Include Logo & Images)

And whatever other bonuses you'd like to kick in associated with the package.

I've attached some images and I've got hundreds more. If you want something else in the way of images, let me know.

I look forward to your seeing your designs.
Updates

Thought I should just clarify the follwoing:

1. The Invoice Header is just a branding for the top of my accounting package form.  It is not contain any contact information or the like.  Just logo, some images and some of your creativity and flair to bring it together.
2. The business does synthetic grass (75% of the business), Wetpour Rubber Surfaces, Softfall Surfaces and Rubber Wood Mulch.  These are categories you might choose to somehow highlight on the letterhead.
3. Business Card reverse side should be used to highlight the categories using images provided.

Wow, I've had some really nice designs submitted thus far, but my concern is that I can't just have an awesome looking card.  I really feel that my card needs to either show or say what we do.  Please make sure your design either shows or says the following:

- Synthetic Grass
- Wetpour Rubber Surfaces
- Softfall Surfaces
- Rubber Wood Mulch
- Shade Structures
- Landscape Structures

Just another note, don't know if I mentioned it or not in the original brief, but I prefer the use of icons instead of text for phone, email, fax etc labels.

Industry/Entity Type

Business

Requirements
Must have
• - Provide full editable source files
- Provide letterhead in MS Word format as well
- All designs must be awesome, but also show or say what we do. This is very important to me. I want anyone to look at our letterhead, business card etc and know instantly what it is that we do.
- Super quick turnaround on handover. I need card files to the printer on Monday morning (that's my Monday at GMT+10)
Nice to have
• - Creative use of the logo for a little bit of wow
Should not have
• - not square, boxy or rigid ... Loosen up a bit!

```html
<!DOCTYPE html>
<html lang="en">
<head>
<meta charset="utf-8">
<title>Copper Lantern Stationery Set</title>
<link rel="stylesheet" href="https://fonts.googleapis.com/css2?family=Exo+2:wght@700&family=Arimo:wght@400;700&display=swap">
<style>
  :root{
    --bg:#1d1d1d;
    --paper:#ffffff;
    --blue:#2a9fd8;
    --blue-dark:#1a7fc0;
    --green:#39b54a;
    --lime:#8dc63f;
    --ink:#333333;
    --muted:#777777;
    --faint:#eef5ea;
    --mulch:#8a6b4c;
    --wetpour:#d8b43c;
    --softfall:#3c6db3;
    --grass:#4f8c4b;
  }
  *{box-sizing:border-box;margin:0;padding:0}
  html,body{width:1200px;height:553px;overflow:hidden;background:var(--bg)}
  body{font-family:"Arimo",Arial,sans-serif;color:var(--ink)}
  .stage{position:absolute;left:0;top:0;width:1390px;height:641px;transform:scale(0.86331);transform-origin:0 0}
  .abs{position:absolute}
  .label{position:absolute;color:#fff;font-size:13px;transform:translateX(-50%);white-space:nowrap}
  .label.big{font-size:15px}
  .sheet{position:absolute;background:var(--paper);overflow:hidden}
  .wave{position:absolute;left:0;bottom:0;width:100%}
  .brand{display:flex;align-items:center;gap:6px;position:absolute}
  .brand-dot{border-radius:50%;border:3px solid var(--blue);flex:none}
  .brand-name{font-family:"Exo 2",sans-serif;font-weight:700;color:var(--blue);text-transform:uppercase;line-height:.9}
  .tagline{font-family:"Arimo",sans-serif;font-weight:700;color:var(--green);white-space:nowrap}
  .ghost{position:absolute;border-radius:50%;border:10px solid var(--faint)}
  .contact{position:absolute;color:#fff;font-size:5px;line-height:7px;white-space:nowrap}
  .contact span::before{content:"";display:inline-block;width:4px;height:4px;border-radius:50%;background:#fff;margin-right:3px;vertical-align:middle}
  .address{position:absolute;color:#fff;font-size:5px;white-space:nowrap}
  .services{position:absolute;font-size:5px;line-height:6.5px;color:var(--muted);border-left:1px solid #ccc;padding-left:3px}
  .fax-title{position:absolute;left:14px;top:54px;font-size:15px;color:#222}
  .fax-row{position:absolute;left:14px;width:205px;border-bottom:1px solid #888;font-size:4.5px;height:10px;display:flex}
  .fax-row span{flex:1}
  .checks{position:absolute;left:14px;top:134px;display:flex;gap:10px;font-size:4.5px}
  .checks span::before{content:"";display:inline-block;width:5px;height:5px;border:1px solid #555;margin-right:3px;vertical-align:middle}
  .shot{position:absolute}
  .web{position:absolute;font-size:7px;letter-spacing:1.5px;color:#333;white-space:nowrap}
  .card{position:absolute;width:172px;height:106px;border-radius:7px;background:var(--paper);overflow:hidden}
  .card.green{background:radial-gradient(circle at 50% 50%,#6fcf5a,var(--green) 70%)}
  .card.blue{background:radial-gradient(circle at 50% 50%,#5cc0ee,var(--blue) 70%)}
  .cat{position:absolute;font-size:5.5px;white-space:nowrap;color:#333}
  .card.green .cat,.card.blue .cat{color:#fff}
  .pic{position:absolute;width:34px;height:34px;border-radius:50%;border:2px solid #ddd}
  .card.squares .pic{border-radius:5px}
  .vweb{position:absolute;left:86px;top:53px;transform:translate(-50%,-50%) rotate(-90deg);font-size:7px;letter-spacing:1px;white-space:nowrap;color:var(--blue)}
  .card.green .vweb,.card.blue .vweb{color:#fff}
  .stripe{position:absolute;left:76px;top:0;width:20px;height:100%;background:var(--blue)}
  .stripe + .vweb{color:#fff}
  .name-line{position:absolute;font-size:7px;color:var(--blue)}
  .title-line{position:absolute;font-size:5.5px;color:#555}
</style>
</head>
<body>
<svg width="0" height="0" style="position:absolute" aria-hidden="true">
  <defs>
    <linearGradient id="g-green" x1="0" x2="1" y1="0" y2="0">
      <stop offset="0" stop-color="#8dc63f"/><stop offset="1" stop-color="#1fa64a"/>
    </linearGradient>
    <linearGradient id="g-blue" x1="0" x2="1" y1="0" y2="1">
      <stop offset="0" stop-color="#5cc6f0"/><stop offset="1" stop-color="#1a7fc0"/>
    </linearGradient>
  </defs>
</svg>

<main class="stage">

  <!-- Presentation folder -->
  <p class="label big" style="left:272px;top:22px">A4 Presentation Folder Design</p>
  <section class="folder">
    <div class="sheet" style="left:40px;top:48px;width:232px;height:330px">
      <div class="brand" style="left:30px;top:16px">
        <span class="brand-dot" style="width:46px;height:46px"></span>
        <span class="brand-name" style="font-size:22px">Copper<br>Lantern</span>
      </div>
      <p class="tagline abs" style="left:84px;top:62px;font-size:6px">Synthetic Grass &amp; Softfall Rubber Surfaces</p>
      <div class="ghost" style="left:58px;top:132px;width:120px;height:120px"></div>
      <svg class="wave" viewBox="0 0 232 42" preserveAspectRatio="none" height="42">
        <path d="M0 20 Q110 0 232 6 L232 42 L0 42Z" fill="url(#g-green)"/>
        <path d="M0 16 Q110 -4 232 2" stroke="var(--blue)" stroke-width="1.5" fill="none"/>
      </svg>
      <div class="contact" style="left:172px;top:302px">
        <span>123-456-789</span><br><span>123-456-7890</span><br><span>hello@copperlantern.com</span><br><span>www.copperlantern.com</span>
      </div>
    </div>
    <svg class="abs" style="left:40px;top:378px" width="232" height="67" viewBox="0 0 232 67">
      <path d="M0 0 H232 L208 67 H0Z" fill="#fff"/>
      <circle cx="100" cy="32" r="17" fill="none" stroke="var(--blue)" stroke-width="3"/>
    </svg>

    <div class="sheet" style="left:272px;top:48px;width:235px;height:330px">
      <div class="brand" style="left:26px;top:136px">
        <span class="brand-dot" style="width:48px;height:48px"></span>
        <span class="brand-name" style="font-size:23px">Copper<br>Lantern</span>
      </div>
      <p class="tagline abs" style="left:82px;top:182px;font-size:6px">Synthetic Grass &amp; Softfall Rubber Surfaces</p>
    </div>
    <svg class="abs" style="left:272px;top:378px" width="235" height="67" viewBox="0 0 235 67">
      <path d="M0 0 H235 V67 H33Z" fill="url(#g-blue)"/>
      <path d="M0 0 H235" stroke="#fff" stroke-width="1"/>
      <circle cx="125" cy="32" r="17" fill="none" stroke="#fff" stroke-width="3"/>
    </svg>
  </section>

  <!-- Letterhead -->
  <p class="label big" style="left:639px;top:27px">A4 Letter head</p>
  <section class="sheet" style="left:523px;top:52px;width:233px;height:330px">
    <div class="brand" style="left:12px;top:10px">
      <span class="brand-dot" style="width:24px;height:24px;border-width:2px"></span>
      <span class="brand-name" style="font-size:11px">Copper<br>Lantern</span>
    </div>
    <p class="tagline abs" style="left:42px;top:34px;font-size:3.5px">Synthetic Grass &amp; Softfall Rubber Surfaces</p>
    <div class="services" style="left:168px;top:12px">
      Synthetic Grass<br>Wetpour Rubber Surfaces<br>Softfall Surfaces<br>Rubber Wood Mulch
    </div>
    <div class="ghost" style="left:57px;top:118px;width:120px;height:120px"></div>
    <svg class="wave" viewBox="0 0 233 44" preserveAspectRatio="none" height="44">
      <path d="M0 22 Q110 0 233 8 L233 44 L0 44Z" fill="url(#g-green)"/>
      <path d="M0 18 Q110 -4 233 4" stroke="var(--blue)" stroke-width="1.5" fill="none"/>
    </svg>
    <div class="contact" style="left:180px;top:300px">
      <span>123-456-789</span><br><span>123-456-7890</span><br><span>hello@copperlantern.com</span><br><span>www.copperlantern.com</span>
    </div>
    <p class="address" style="left:14px;top:322px">00, Complex name, City, State 0040</p>
  </section>

  <!-- Fax sheet -->
  <p class="label big" style="left:893px;top:27px">A4 Fax sheet</p>
  <section class="sheet" style="left:778px;top:52px;width:233px;height:330px">
    <div class="brand" style="left:64px;top:10px">
      <span class="brand-dot" style="width:24px;height:24px;border-width:2px"></span>
      <span class="brand-name" style="font-size:11px">Copper<br>Lantern</span>
    </div>
    <p class="tagline abs" style="left:94px;top:34px;font-size:3.5px">Synthetic Grass &amp; Softfall Rubber Surfaces</p>
    <h1 class="fax-title">FAX</h1>
    <div class="fax-row" style="top:72px"><span>To :</span><span>From :</span></div>
    <div class="fax-row" style="top:85px"><span>Fax :</span><span>Pages :</span></div>
    <div class="fax-row" style="top:98px"><span>Phone :</span><span>Date :</span></div>
    <div class="fax-row" style="top:111px"><span>Re :</span><span>CC :</span></div>
    <div class="checks"><span>Urgent</span><span>For Review</span><span>Please Comment</span><span>Please Reply</span><span>Please Recycle</span></div>
    <svg class="wave" viewBox="0 0 233 44" preserveAspectRatio="none" height="44">
      <path d="M0 22 Q110 0 233 8 L233 44 L0 44Z" fill="url(#g-green)"/>
      <path d="M0 18 Q110 -4 233 4" stroke="var(--blue)" stroke-width="1.5" fill="none"/>
    </svg>
    <div class="contact" style="left:180px;top:300px">
      <span>123-456-789</span><br><span>123-456-7890</span><br><span>hello@copperlantern.com</span><br><span>00, Complex name, City, State 0040</span>
    </div>
  </section>

  <!-- Envelopes -->
  <p class="label big" style="left:1058px;top:141px">Envelop</p>
  <section class="envelopes">
    <svg class="abs" style="left:1090px;top:62px" width="272" height="176" viewBox="0 0 272 176">
      <rect width="272" height="176" fill="#fff"/>
      <path d="M0 0 H272 V10 Q250 30 160 48 Q136 54 112 48 Q22 30 0 10Z" fill="url(#g-blue)"/>
      <circle cx="136" cy="24" r="12" fill="none" stroke="#fff" stroke-width="2.5"/>
      <path d="M0 50 H272 V62 Q250 82 160 100 Q136 106 112 100 Q22 82 0 62Z" fill="url(#g-green)"/>
      <circle cx="136" cy="78" r="12" fill="none" stroke="#fff" stroke-width="2.5"/>
    </svg>
    <svg class="abs" style="left:1032px;top:172px" width="270" height="60" viewBox="0 0 270 60">
      <rect width="270" height="60" fill="#fff"/>
      <path d="M0 0 Q40 30 120 44 Q135 47 150 44 Q230 30 270 0" stroke="#ccc" fill="none"/>
      <circle cx="133" cy="23" r="12" fill="none" stroke="var(--blue)" stroke-width="2.5"/>
    </svg>
    <div class="sheet" style="left:1045px;top:222px;width:275px;height:126px">
      <div class="brand" style="left:12px;top:12px">
        <span class="brand-dot" style="width:28px;height:28px"></span>
        <span class="brand-name" style="font-size:13px">Copper<br>Lantern</span>
      </div>
      <p class="tagline abs" style="left:46px;top:39px;font-size:4px">Synthetic Grass &amp; Softfall Rubber Surfaces</p>
      <p class="abs" style="left:12px;top:58px;font-size:5px;color:#888">00, Complex name, City, State 0040</p>
      <svg class="wave" viewBox="0 0 275 50" preserveAspectRatio="none" height="50">
        <path d="M0 38 Q150 30 275 0 L275 50 L0 50Z" fill="url(#g-green)"/>
        <path d="M0 34 Q150 26 275 -4" stroke="var(--blue)" stroke-width="1.5" fill="none"/>
        <circle cx="240" cy="33" r="9" fill="none" stroke="#fff" stroke-width="2"/>
      </svg>
      <p class="abs" style="left:50px;top:116px;font-size:5px;color:#fff;letter-spacing:1px">www.copperlantern.com</p>
    </div>
  </section>

  <!-- Invoice headers -->
  <p class="label big" style="left:667px;top:391px">Invoice Header # 1</p>
  <section class="sheet" style="left:542px;top:413px;width:228px;height:60px">
    <div class="brand" style="left:8px;top:15px">
      <span class="brand-dot" style="width:18px;height:18px;border-width:2px"></span>
      <span class="brand-name" style="font-size:8px">Copper<br>Lantern</span>
    </div>
    <div class="shot" role="img" aria-label="Playground with wetpour rubber surface" style="left:81px;top:10px;width:32px;height:32px;background:linear-gradient(135deg,var(--wetpour),var(--blue))"></div>
    <div class="shot" role="img" aria-label="Rubber wood mulch under play equipment" style="left:118px;top:10px;width:32px;height:32px;background:linear-gradient(135deg,var(--mulch),#b5523a)"></div>
    <div class="shot" role="img" aria-label="Synthetic grass lawn" style="left:156px;top:10px;width:32px;height:32px;background:linear-gradient(135deg,#6fae5a,var(--grass))"></div>
    <div class="shot" role="img" aria-label="Softfall surface with playground figure" style="left:194px;top:10px;width:32px;height:32px;background:linear-gradient(135deg,var(--softfall),#e0a63a)"></div>
    <p class="web" style="left:70px;top:48px">www.copperlantern.com</p>
  </section>

  <p class="label big" style="left:884px;top:391px">Invoice Header # 2</p>
  <section class="sheet" style="left:789px;top:414px;width:233px;height:60px">
    <div class="shot" role="img" aria-label="Rubber wood mulch area" style="left:8px;top:5px;width:36px;height:24px;background:linear-gradient(135deg,var(--mulch),#b5523a)"></div>
    <div class="shot" role="img" aria-label="Wetpour rubber playground" style="left:8px;top:33px;width:36px;height:24px;background:linear-gradient(135deg,var(--wetpour),var(--blue))"></div>
    <div class="brand" style="left:60px;top:14px">
      <span class="brand-dot" style="width:26px;height:26px"></span>
      <span class="brand-name" style="font-size:12px">Copper<br>Lantern</span>
    </div>
    <p class="tagline abs" style="left:92px;top:38px;font-size:4px">Synthetic Grass &amp; Softfall Rubber Surfaces</p>
    <div class="shot" role="img" aria-label="Softfall surface with playground figure" style="left:186px;top:5px;width:32px;height:22px;background:linear-gradient(135deg,var(--softfall),#e0a63a)"></div>
    <div class="shot" role="img" aria-label="Synthetic grass lawn" style="left:186px;top:32px;width:32px;height:22px;background:linear-gradient(135deg,#6fae5a,var(--grass))"></div>
    <p class="web" style="left:72px;top:49px;font-size:6px">www.copperlantern.com</p>
  </section>

  <!-- Email signature -->
  <section class="sheet" style="left:1045px;top:417px;width:145px;height:45px">
    <div class="brand" style="left:5px;top:4px">
      <span class="brand-dot" style="width:14px;height:14px;border-width:2px"></span>
      <span class="brand-name" style="font-size:7px">Copper<br>Lantern</span>
    </div>
    <p class="abs" style="left:6px;top:24px;font-size:3.5px;color:#888">00, Complex name, City, State 0040</p>
    <p class="abs" style="left:104px;top:5px;font-size:7px;color:var(--green);font-weight:700">Your name</p>
    <p class="abs" style="left:118px;top:14px;font-size:5px;color:#666">Title</p>
    <svg class="wave" viewBox="0 0 145 14" preserveAspectRatio="none" height="14">
      <path d="M0 10 Q80 8 145 0 L145 14 L0 14Z" fill="url(#g-green)"/>
    </svg>
  </section>
  <p class="label" style="left:1116px;top:467px;font-size:14px">Email signature</p>

  <!-- Business cards -->
  <section class="card" style="left:47px;top:497px">
    <div class="brand" style="left:12px;top:10px">
      <span class="brand-dot" style="width:26px;height:26px"></span>
      <span class="brand-name" style="font-size:12px">Copper<br>Lantern</span>
    </div>
    <p class="tagline abs" style="left:44px;top:36px;font-size:4px">Synthetic Grass &amp; Softfall Rubber Surfaces</p>
    <p class="abs" style="left:12px;top:55px;font-size:5px;color:#666">● 00, Complex name, City, State 0040</p>
    <svg class="wave" viewBox="0 0 172 40" preserveAspectRatio="none" height="40">
      <path d="M0 28 Q100 24 172 0 L172 40 L0 40Z" fill="url(#g-green)"/>
    </svg>
    <p class="name-line" style="left:12px;top:66px">Your name</p>
    <p class="title-line" style="left:12px;top:75px">Title</p>
    <div class="contact" style="left:126px;top:74px;font-size:4.5px;line-height:6px">
      <span>123-456-789</span><br><span>123-456-7890</span><br><span>hello@copperlantern.com</span><br><span>www.copperlantern.com</span>
    </div>
  </section>

  <section class="card" style="left:230px;top:497px">
    <span class="abs" style="left:53px;top:14px;width:64px;height:64px;border-radius:50%;border:5px solid var(--blue)"></span>
    <p class="web" style="left:38px;top:92px;font-size:6px">www.copperlantern.com</p>
  </section>

  <!-- Card back 2 -->
  <section class="card" style="left:415px;top:497px">
    <p class="cat" style="left:6px;top:6px">Rubber Wood Mulch</p>
    <p class="cat" style="right:6px;top:6px">Wetpour Rubber Surfaces</p>
    <p class="cat" style="left:8px;top:54px">Softfall Surfaces</p>
    <p class="cat" style="right:18px;top:54px">Synthetic Grass</p>
    <div class="pic" role="img" aria-label="Rubber wood mulch" style="left:20px;top:15px;background:var(--mulch)"></div>
    <div class="pic" role="img" aria-label="Wetpour rubber surface" style="left:118px;top:15px;background:linear-gradient(135deg,var(--wetpour),var(--blue))"></div>
    <div class="pic" role="img" aria-label="Softfall surface" style="left:20px;top:63px;background:linear-gradient(135deg,var(--softfall),#e0a63a)"></div>
    <div class="pic" role="img" aria-label="Synthetic grass" style="left:118px;top:63px;background:var(--grass)"></div>
    <p class="vweb">www.copperlantern.com</p>
  </section>

  <!-- Card back 3 -->
  <section class="card" style="left:600px;top:497px">
    <div class="stripe"></div>
    <p class="vweb">www.copperlantern.com</p>
    <p class="cat" style="left:6px;top:6px">Rubber Wood Mulch</p>
    <p class="cat" style="right:6px;top:6px">Wetpour Rubber Surfaces</p>
    <p class="cat" style="left:8px;top:54px">Softfall Surfaces</p>
    <p class="cat" style="right:18px;top:54px">Synthetic Grass</p>
    <div class="pic" role="img" aria-label="Rubber wood mulch" style="left:20px;top:15px;background:var(--mulch)"></div>
    <div class="pic" role="img" aria-label="Wetpour rubber surface" style="left:118px;top:15px;background:linear-gradient(135deg,var(--wetpour),var(--blue))"></div>
    <div class="pic" role="img" aria-label="Softfall surface" style="left:20px;top:63px;background:linear-gradient(135deg,var(--softfall),#e0a63a)"></div>
    <div class="pic" role="img" aria-label="Synthetic grass" style="left:118px;top:63px;background:var(--grass)"></div>
  </section>

  <!-- Card back 4 -->
  <section class="card green" style="left:782px;top:497px">
    <p class="cat" style="left:6px;top:6px">Rubber Wood Mulch</p>
    <p class="cat" style="right:6px;top:6px">Wetpour Rubber Surfaces</p>
    <p class="cat" style="left:8px;top:54px">Softfall Surfaces</p>
    <p class="cat" style="right:18px;top:54px">Synthetic Grass</p>
    <div class="pic" role="img" aria-label="Rubber wood mulch" style="left:20px;top:15px;background:var(--mulch)"></div>
    <div class="pic" role="img" aria-label="Wetpour rubber surface" style="left:118px;top:15px;background:linear-gradient(135deg,var(--wetpour),var(--blue))"></div>
    <div class="pic" role="img" aria-label="Softfall surface" style="left:20px;top:63px;background:linear-gradient(135deg,var(--softfall),#e0a63a)"></div>
    <div class="pic" role="img" aria-label="Synthetic grass" style="left:118px;top:63px;background:var(--grass)"></div>
    <p class="vweb">www.copperlantern.com</p>
  </section>

  <!-- Card back 5 -->
  <section class="card blue" style="left:967px;top:497px">
    <p class="cat" style="left:6px;top:6px">Rubber Wood Mulch</p>
    <p class="cat" style="right:6px;top:6px">Wetpour Rubber Surfaces</p>
    <p class="cat" style="left:8px;top:54px">Softfall Surfaces</p>
    <p class="cat" style="right:18px;top:54px">Synthetic Grass</p>
    <div class="pic" role="img" aria-label="Rubber wood mulch" style="left:20px;top:15px;background:var(--mulch)"></div>
    <div class="pic" role="img" aria-label="Wetpour rubber surface" style="left:118px;top:15px;background:linear-gradient(135deg,var(--wetpour),var(--blue))"></div>
    <div class="pic" role="img" aria-label="Softfall surface" style="left:20px;top:63px;background:linear-gradient(135deg,var(--softfall),#e0a63a)"></div>
    <div class="pic" role="img" aria-label="Synthetic grass" style="left:118px;top:63px;background:var(--grass)"></div>
    <p class="vweb">www.copperlantern.com</p>
  </section>

  <!-- Card back 6 -->
  <section class="card squares" style="left:1157px;top:497px">
    <p class="cat" style="left:6px;top:6px">Rubber Wood Mulch</p>
    <p class="cat" style="right:6px;top:6px">Wetpour Rubber Surfaces</p>
    <p class="cat" style="left:8px;top:54px">Softfall Surfaces</p>
    <p class="cat" style="right:18px;top:54px">Synthetic Grass</p>
    <div class="pic" role="img" aria-label="Rubber wood mulch" style="left:14px;top:15px;width:40px;background:var(--mulch)"></div>
    <div class="pic" role="img" aria-label="Wetpour rubber surface" style="left:118px;top:15px;width:40px;background:linear-gradient(135deg,var(--wetpour),var(--blue))"></div>
    <div class="pic" role="img" aria-label="Softfall surface" style="left:14px;top:63px;width:40px;background:linear-gradient(135deg,var(--softfall),#e0a63a)"></div>
    <div class="pic" role="img" aria-label="Synthetic grass" style="left:118px;top:63px;width:40px;background:var(--grass)"></div>
    <p class="vweb">www.copperlantern.com</p>
  </section>

  <p class="label big" style="left:133px;top:611px">Front</p>
  <p class="label big" style="left:314px;top:611px">Back # 1</p>
  <p class="label big" style="left:505px;top:611px">Back # 2</p>
  <p class="label big" style="left:686px;top:611px">Back # 3</p>
  <p class="label big" style="left:864px;top:611px">Back # 4</p>
  <p class="label big" style="left:1051px;top:611px">Back # 5</p>
  <p class="label big" style="left:1238px;top:611px">Back # 6</p>

</main>
</body>
</html>
```